Looking for a cool, modern Cannabis Jar Label

I want you to come up with a better, modern look for a label.

I need it sized to 4” x 3” - I plan to print directly to label printer.

I want you to use Photoshop and deliver me a layered PSD file that I can edit and modify the information as needed..

The label information will need to include places for:
(1) Strain Name - most important part of label - larger font size than rest - example Marlow Frost, KTV #7, Copperleaf Haze
(2) Pricing - for Gram, 1/8, 1/4, 1/2. and Ounce
(3) Strain Designation (Hybrid, Indica or Sativa) - maybe color coded, different color for Indica v. Sativa, just an idea
(4) THC and CBD percentages - for example 23% THC and 0.05% CBD
(5) Farm name - a place where we can add the name/logo of the business that produced the product. example - Bramwell Farms

I have attached a simple mockup showing the information.

I have also attached a few samples of labels we like to give you an idea of the look and feel we are going for.

I am wanting a very clean, modern, classy, readable look.The font will use is Gotham Font.

HI Everyone! Thank you for all of your designs. I am requesting an extension because I need more time to give adequate feedback to the designers. Thank you for your participation and all of your efforts! I will be making a decision soon!

• Gotham Font

Designer to choose colors to be used in the design.

• Thank you for your designs. I am sorry i have been slow in providing feedback, things have been really busy around here!
• I wanted to give some group general feedback. After reviewing all of the designs, there is a common theme among all of the designs that I would like to see changed.
• I would like to see the per gram pricing more prominent on the label. This is what most people are looking for when they are purchasing the product. So I would like to see this stand out from the other pricing tiers. As I think about it, they don't all need to be grouped together in a line. You could have the Per Gram pricing front and center some where and then the other pricing tiers grouped together somewhere else on the label.
• This is the order of importance of items on the label. Items at the the top of the list should be bigger than those below it.
• 1. Strain name
• 2. Pricing - being per gram the most important of all prices
• 3. THC/CBD percentages
• 4. Strain Type (indica, sativa, hybrid)
• 5. Farm name/logo
• When laying out these labels, they will be going on rounded jars and they will be on display. Think of jars with fancy labels in a candy store. They need to be eye catchy, appealing, but easy read.
• Thank you for all of your hard work, everyone is doing a great job.
• Best,
• Nadia

```html
<!DOCTYPE html>
<html lang="en">
<head>
<meta charset="utf-8">
<title>Cedar Ridge Frost – Jar Label</title>
<link href="https://fonts.googleapis.com/css2?family=Ultra&family=Montserrat:wght@300;400;700;800&display=swap" rel="stylesheet">
<style>
  :root {
    --page-bg: #c4c4c4;
    --label-bg: #f4f4f4;
    --ink: #2f2f2f;
    --orange: #f29a1f;
    --gold-light: #f3d9a6;
    --gold-dark: #b88842;
    --cream: #fbf3e8;
    --cream-deep: #e9d6bd;
    --rule: #b9b9b9;
    --jar-green: #2e8b4a;
  }
  * { box-sizing: border-box; margin: 0; padding: 0; }
  html, body { width: 1200px; height: 545px; overflow: hidden; }
  body { background: var(--page-bg); font-family: "Montserrat", sans-serif; color: var(--ink); }

  .label {
    position: absolute; left: 258px; top: 17px;
    width: 684px; height: 510px;
    background: linear-gradient(160deg, #fafafa 0%, var(--label-bg) 55%, #ececec 100%);
    overflow: hidden;
  }

  .strain-frame {
    position: absolute; left: 16px; top: 15px; width: 649px; height: 177px;
    border: 3px solid var(--orange); border-radius: 20px;
  }
  .strain-name {
    position: absolute; left: 0; right: 0; top: 14px;
    font-family: "Ultra", "Rockwell", serif; font-weight: 400;
    font-size: 54px; line-height: 60px; letter-spacing: 2px;
    text-align: center; text-transform: uppercase; color: var(--ink);
  }

  .strain-type {
    position: absolute; left: 232px; top: 166px; width: 224px; height: 46px;
    background: var(--orange); border-radius: 23px;
    font-family: "Ultra", "Rockwell", serif; font-size: 28px; line-height: 46px;
    letter-spacing: 2px; text-align: center; color: #fff;
  }
  .type-flourish {
    position: absolute; left: 296px; top: 212px; width: 96px; height: 18px;
    background: radial-gradient(ellipse at center top, rgba(242,154,31,.55), rgba(242,154,31,0) 70%);
  }

  .divider {
    position: absolute; left: 16px; width: 649px; height: 6px;
    border-top: 1px solid var(--rule); border-bottom: 1px solid var(--rule);
  }
  .divider.top { top: 236px; }
  .divider.bottom { top: 377px; }

  .price-row {
    position: absolute; left: 16px; top: 243px; width: 649px; height: 130px;
    display: flex; align-items: center; justify-content: space-between;
  }
  .price-badge {
    width: 112px; height: 112px; border-radius: 50%;
    background: linear-gradient(145deg, var(--gold-light), var(--gold-dark) 55%, var(--gold-light));
    padding: 5px; flex: none;
  }
  .price-badge .face {
    width: 100%; height: 100%; border-radius: 50%;
    background: radial-gradient(circle at 50% 35%, var(--cream) 0%, #f5e8d6 55%, var(--cream-deep) 100%);
    display: flex; flex-direction: column; align-items: center; justify-content: center;
  }
  .tier { font-weight: 700; font-size: 23px; line-height: 26px; }
  .amount { font-weight: 800; font-size: 28px; line-height: 32px; white-space: nowrap; }
  .amount sup { font-weight: 400; font-size: 15px; vertical-align: 10px; margin-left: 2px; }

  .price-badge.per-gram {
    width: 130px; height: 130px; padding: 6px;
    background: var(--orange);
  }
  .price-badge.per-gram .tier { font-size: 25px; color: var(--orange); }
  .price-badge.per-gram .amount { font-size: 34px; line-height: 38px; }
  .price-badge.per-gram .amount sup { font-size: 18px; vertical-align: 12px; }

  .potency-row {
    position: absolute; left: 16px; top: 400px; width: 649px; height: 68px;
    display: flex; align-items: center;
  }
  .jar-icon { width: 22px; height: 42px; flex: none; margin-right: 4px; }
  .potency-value {
    font-weight: 300; font-size: 56px; line-height: 64px;
    letter-spacing: -1px; color: var(--ink); white-space: nowrap;
  }
  .potency-unit {
    width: 16px; margin: 0 8px 0 4px; align-self: flex-start; margin-top: 6px;
    font-weight: 700; font-size: 14px; line-height: 17px; text-align: center; color: var(--orange);
  }

  .farm {
    margin-left: auto; height: 48px;
    display: flex; align-items: center; gap: 8px;
  }
  .farm-mark { width: 40px; height: 40px; border-radius: 50%; border: 2px solid var(--ink); flex: none; }
  .farm-name {
    font-weight: 800; font-size: 19px; line-height: 21px; color: var(--ink);
    text-transform: uppercase;
  }

  .bottom-tab {
    position: absolute; left: 232px; top: 488px; width: 224px; height: 30px;
    background: var(--orange); border-radius: 15px 15px 0 0;
  }
</style>
</head>
<body>
  <main class="label">
    <section class="strain-frame">
      <h1 class="strain-name">Cedar Ridge<br>Frost</h1>
    </section>
    <div class="strain-type">INDICA</div>
    <div class="type-flourish" role="img" aria-label="Small ornamental flourish under the strain type"></div>

    <div class="divider top"></div>

    <section class="price-row">
      <div class="price-badge per-gram"><div class="face"><span class="tier">g.</span><span class="amount">25<sup>50</sup></span></div></div>
      <div class="price-badge"><div class="face"><span class="tier">1/8</span><span class="amount">65<sup>00</sup></span></div></div>
      <div class="price-badge"><div class="face"><span class="tier">1/4</span><span class="amount">120<sup>00</sup></span></div></div>
      <div class="price-badge"><div class="face"><span class="tier">1/2</span><span class="amount">230<sup>00</sup></span></div></div>
      <div class="price-badge"><div class="face"><span class="tier">oz</span><span class="amount">430<sup>00</sup></span></div></div>
    </section>

    <div class="divider bottom"></div>

    <section class="potency-row">
      <svg class="jar-icon" viewBox="0 0 22 42" aria-hidden="true">
        <rect x="4" y="0" width="14" height="6" rx="1.5" fill="var(--jar-green)"/>
        <rect x="0" y="8" width="22" height="34" rx="4" fill="var(--jar-green)"/>
        <circle cx="11" cy="25" r="5" fill="#fff"/>
      </svg>
      <span class="potency-value thc">23%</span>
      <span class="potency-unit thc">T<br>H<br>C</span>
      <span class="potency-value cbd">0.05%</span>
      <span class="potency-unit cbd">C<br>B<br>D</span>
      <div class="farm">
        <span class="farm-mark"></span>
        <span class="farm-name">Bramwell<br>Farms</span>
      </div>
    </section>

    <div class="bottom-tab"></div>
  </main>
</body>
</html>
```